EPIC, awesome, creative business card needed - get involved!

I'm launching a boutique, exclusive Property Management real estate agency in Sydney early next year.
The name of the agency will be called "Quartz Hill Lane" - it's a play on "chase the silver pebble trail" to wealth. The Quartz Hill Lane signifies wealth through property investment.
My business will offer management of investment properties (ie Property Management).
The difference with Quartz Hill Lane and other agencies is the business will be run by one of Australia's leading property investment experts, and also one of Australia's leading property managers.
It will be exclusively for high net worth properties and individuals, so the business card needs to be extremely sharp, slick and relatively simple.
The information I want on the card is as follows
Nolan Pryce - Director
M: 0412 967 154
P: 9735 6021
E: nolan@quartzhilllane.net.au
W: quartzhilllane.net.au
I'm happy with the red from the logo, black - no yellows or funky colors. I want this to be a super corporate and slick business card to match the high end nature of the business.
Good luck everyone, and please ask questions for clarification.

```html
<!DOCTYPE html>
<html lang="en">
<head>
<meta charset="utf-8">
<title>Quartz Hill Lane – Business Card</title>
<link rel="stylesheet" href="https://fonts.googleapis.com/css2?family=Pathway+Gothic+One&family=Reenie+Beanie&display=swap">
<style>
  :root {
    --brand-red: #c20000;
    --varnish-red: #a30a0a;
    --paper: #ffffff;
    --ink: #1a1a1a;
    --card-text: #ffffff;
  }
  html, body {
    margin: 0;
    padding: 0;
    overflow: hidden;
    background: var(--paper);
  }
  .sheet {
    position: relative;
    width: 812px;
    height: 1200px;
    overflow: hidden;
    background: var(--paper);
  }

  /* brand name at top */
  .brand-master {
    position: absolute;
    left: 239px;
    top: 34px;
    width: 263px;
    height: 312px;
    display: flex;
    align-items: center;
    justify-content: center;
    gap: 14px;
  }
  .brand-master__square {
    width: 30px;
    height: 30px;
    background: var(--brand-red);
    flex: none;
  }
  .brand-master__name {
    font-family: "Pathway Gothic One", sans-serif;
    font-size: 52px;
    line-height: 1;
    color: var(--brand-red);
    margin: 0;
    white-space: nowrap;
  }

  /* annotation labels */
  .note {
    position: absolute;
    font-family: "Reenie Beanie", cursive;
    font-size: 40px;
    color: var(--ink);
    line-height: 1;
    margin: 0;
  }
  .note--front { left: 50px; top: 415px; }
  .note--varnish { left: 50px; top: 468px; }
  .note--back { left: 398px; top: 468px; }

  /* cards */
  .card {
    position: absolute;
    top: 519px;
    width: 301px;
    height: 489px;
    background: var(--brand-red);
  }
  .card--front { left: 50px; }
  .card--back { left: 398px; }

  .card__brand {
    position: absolute;
    left: 23px;
    top: 165px;
    width: 248px;
    height: 300px;
    display: flex;
    align-items: center;
    justify-content: center;
  }
  .card__brand-name {
    font-family: "Pathway Gothic One", sans-serif;
    font-size: 42px;
    line-height: 1;
    color: var(--varnish-red);
    margin: 0;
    white-space: nowrap;
  }

  .contact {
    position: absolute;
    left: 38px;
    top: 334px;
    margin: 0;
    padding: 0;
    list-style: none;
    font-family: "Pathway Gothic One", sans-serif;
    font-size: 19px;
    line-height: 27.5px;
    color: var(--card-text);
  }
</style>
</head>
<body>
  <main class="sheet">
    <header class="brand-master">
      <span class="brand-master__square"></span>
      <h1 class="brand-master__name">Quartz Hill Lane</h1>
    </header>

    <p class="note note--front">Front</p>
    <p class="note note--varnish">Logo to be varnish</p>
    <p class="note note--back">Back</p>

    <section class="card card--front" aria-label="Card front">
      <div class="card__brand">
        <p class="card__brand-name">Quartz Hill Lane</p>
      </div>
    </section>

    <section class="card card--back" aria-label="Card back">
      <ul class="contact">
        <li>Nolan Pryce - Director</li>
        <li>M: 0412 967 154</li>
        <li>P: 9735 6021</li>
        <li>E: nolan@quartzhilllane.net.au</li>
        <li>W: quartzhilllane.net.au</li>
      </ul>
    </section>
  </main>
</body>
</html>
```